Marcus Fenwick Consulting Webpage

I need to transition into a Wordpress website to be able to insert tracking code. This was a HostVerra website, but now I'm limited on functionality

Here are requirements: I need to replicate marcusfenwick.example

My company is focused in search and placement, consulting and workforce development for the turfgrass and hospitality industry

I'm also looking to integrate the following for a recruiting agency job board.
Multiple Dashboard view
✔ Job map
✔ Demo Content upload
✔ Chat button
✔ CV/Resume builder
✔ Featured job on top
✔ Email Alert
✔ Job bookmark
✔ Job CV package
✔ Social media Login
✔ SEO set up
✔ Plugin installation
✔ Featured jobs
✔ Payment gateway integration and set up
✔ Responsive design

Target Market(s)

Golf and turfgrass businesses; as well as candidates for those companies

Industry/Entity Type

Turfgrass and Golf Industry

Coding

Coded - Design and coding required

Font styles to use
Sans Serif

Colors

Designer to choose colors to be used in the design.

Requirements
Must have
• Functionality of HostVerra Web Design builder, Chat box capability, pop up capability, scheduling/appointment booking integration, ability to upload videos similar to my current website, e-commerce capabilities
Nice to have
• Everything to integrate "recruiting agency" aspect to collect information from potential candidates

```html
<!DOCTYPE html>
<html lang="en">
<head>
<meta charset="utf-8">
<title>Marcus Fenwick Consulting</title>
<link href="https://fonts.googleapis.com/css2?family=Saira+Semi+Condensed:wght@400;500;600;700&family=Poppins:ital,wght@0,400;0,500;0,600;1,400&display=swap" rel="stylesheet">
<style>
:root{
  --blue:#1c64d6;
  --blue-dark:#1550b3;
  --ink:#3d4248;
  --muted:#6f757b;
  --soft:#f6f7fa;
  --line:#e6e8ec;
  --footer:#262d33;
  --green:#3cb24a;
  --orange:#f26a1b;
  --white:#fff;
}
*{box-sizing:border-box;margin:0;padding:0}
html,body{width:1200px;height:3610px;overflow:hidden}
body{position:relative;background:var(--white);font-family:"Poppins",sans-serif;color:var(--ink)}
.abs{position:absolute}
.cond{font-family:"Saira Semi Condensed","Arial Narrow",sans-serif}
.head{font-family:"Saira Semi Condensed","Arial Narrow",sans-serif;font-weight:600;letter-spacing:1.5px;text-transform:uppercase;white-space:nowrap}
.center{text-align:center}
.btn{position:absolute;display:flex;align-items:center;justify-content:center;gap:6px;background:var(--blue);color:#fff;font-family:"Saira Semi Condensed","Arial Narrow",sans-serif;font-weight:600;letter-spacing:1px;font-size:14px;white-space:nowrap}
.lead{font-size:13px;line-height:20px;color:var(--muted)}

/* header */
.topbar{top:0;left:0;width:1200px;height:78px;background:#fff}
.brand{top:0;left:60px;width:170px;height:155px;background:#fff;clip-path:polygon(0 0,100% 0,100% 83%,0 100%);z-index:3;display:flex;flex-direction:column;align-items:center;padding-top:22px}
.brand-dot{width:30px;height:30px;border-radius:50%;background:#3e4a48;margin-bottom:12px}
.brand-name{font-family:"Saira Semi Condensed","Arial Narrow",sans-serif;font-weight:600;font-size:15px;color:#3e4a48;text-align:center;line-height:17px;text-transform:uppercase}
.nav-link{position:absolute;top:33px;font-family:"Saira Semi Condensed","Arial Narrow",sans-serif;font-weight:600;font-size:12px;color:#2c3136;white-space:nowrap}
.nav-link.on{color:var(--blue-dark)}
.auth{top:33px;font-family:"Saira Semi Condensed","Arial Narrow",sans-serif;font-weight:600;font-size:12px;color:var(--blue);white-space:nowrap}

/* hero */
.hero{top:78px;left:0;width:1200px;height:418px;background:linear-gradient(180deg,#6562ad 0%,#5b57a6 45%,#6f6cb3 100%)}
.hero-title{top:176px;left:0;width:1200px;color:#fff;font-size:32px;line-height:31px;letter-spacing:3px}
.search{top:265px;left:275px;width:730px;height:46px;background:#fff;display:flex;align-items:center;font-size:10.5px;color:#444}
.search .f{height:100%;display:flex;align-items:center;padding-left:20px;border-right:1px solid var(--line);white-space:nowrap}
.search .go{margin-left:auto;width:79px;height:100%;background:var(--blue);display:flex;align-items:center;justify-content:center}
.ghost{top:333px;height:44px;border:1px solid rgba(255,255,255,.7);background:rgba(70,64,150,.35);color:#fff;font-size:12px;font-weight:500;display:flex;align-items:center;justify-content:center;gap:8px;white-space:nowrap}

/* stats */
.stat{top:522px;width:220px;text-align:center}
.stat b{display:block;font-family:"Saira Semi Condensed","Arial Narrow",sans-serif;font-weight:500;font-size:34px;line-height:36px;color:#2f3438}
.stat i{font-style:normal;font-size:14px;color:var(--blue);letter-spacing:.5px;font-weight:500}
.vline{top:530px;width:1px;height:52px;background:var(--line)}

/* section titles */
.title{left:0;width:1200px;text-align:center;font-size:28px;color:#4a4f55}
.title em{font-style:normal;color:var(--blue)}

/* categories */
.cat{top:786px;width:260px;text-align:center}
.cat-art{width:86px;height:62px;margin:0 auto 14px;border-radius:32px 8px 32px 8px;background:linear-gradient(135deg,#cfe0f7,#7fa9e6)}
.cat h4{font-weight:500;font-size:17px;letter-spacing:1px;color:#33383d;white-space:nowrap}
.cat p{font-size:12px;letter-spacing:1px;color:#555;margin-top:2px}

/* promo */
.promo{top:1055px;left:0;width:1200px;height:485px;background:var(--soft)}
.promo-title{top:1166px;left:158px;font-size:26px;line-height:29px;color:#4a4f55}
.tablet{top:1139px;left:601px;width:444px;height:313px;background:#fff;border-radius:14px;box-shadow:0 2px 10px rgba(0,0,0,.12);border:1px solid #ddd}
.tablet-screen{top:1155px;left:635px;width:373px;height:279px;background:linear-gradient(135deg,#9fd2ef,#6fb8e6 60%,#a6d8f1)}

/* jobs */
.job{height:115px;width:434px;border:1px solid var(--line);background:#fff}
.job .logo{position:absolute;left:0;top:0;width:102px;height:100%;border-right:1px solid var(--line);display:flex;align-items:center;justify-content:center}
.job .name{position:absolute;left:117px;top:18px;font-family:"Saira Semi Condensed","Arial Narrow",sans-serif;font-weight:600;font-size:14px;color:#2f3438;white-space:nowrap}
.job .pub{position:absolute;left:117px;top:40px;font-size:12px;color:#8a9096}
.job .meta{position:absolute;left:119px;top:86px;font-size:11px;color:#9aa0a5;display:flex;gap:10px;align-items:center;white-space:nowrap}
.job .meta small{font-size:9.5px}
.job .tag{position:absolute;left:325px;top:80px;width:86px;height:22px;color:#fff;font-family:"Saira Semi Condensed","Arial Narrow",sans-serif;font-weight:600;font-size:10px;letter-spacing:.5px;display:flex;align-items:center;justify-content:center}
.job .heart{position:absolute;right:32px;top:20px}

/* research */
.research-bg{top:2048px;left:426px;width:715px;height:485px;background:var(--soft)}
.research-photo{top:2100px;left:111px;width:474px;height:381px;background:linear-gradient(180deg,#9bb4c4 0%,#6d8a5a 35%,#86b04a 55%,#5a7a3a 75%,#7a3a4a 100%)}
.research-title{top:2148px;left:638px;font-size:26px;line-height:29px;color:#4a4f55}

/* testimonials */
.quote{top:2724px;width:240px;text-align:center}
.avatar{width:88px;height:88px;border-radius:50%;border:1px solid #ddd;background:#fff;margin:0 auto;position:relative;display:flex;align-items:center;justify-content:center}
.avatar .badge{width:56px;height:56px;border-radius:50%;background:#e7ecf3}
.avatar .q{position:absolute;right:-8px;bottom:-4px;width:34px;height:34px;border-radius:50%;background:var(--blue);color:#fff;font-family:Georgia,serif;font-size:30px;line-height:44px;font-weight:700}
.quote p{margin-top:16px;font-size:13px;font-style:italic;line-height:19px;color:#777}
.quote h5{margin-top:12px;font-size:15px;font-style:italic;font-weight:600;color:var(--blue)}
.quote small{display:block;font-size:11px;font-style:italic;color:#777;margin-top:2px}
.seen{top:3052px;width:165px;height:88px;border:1px solid #eee;border-radius:6px;display:flex;align-items:center;justify-content:center;box-shadow:0 1px 4px rgba(0,0,0,.04)}
.seen span{width:62px;height:62px;border-radius:50%;background:#dfe6dc}

/* footer */
.footer{top:3205px;left:0;width:1200px;height:405px;background:var(--footer);color:#d9dde1}
.foot-brand{top:3205px;left:159px;width:171px;height:135px;background:#fff;clip-path:polygon(0 0,100% 0,100% 88%,0 100%);display:flex;flex-direction:column;align-items:center;padding-top:20px}
.fcol{top:3276px}
.fcol h6{font-family:"Poppins",sans-serif;font-weight:600;font-size:14px;letter-spacing:1px;color:#fff;margin-bottom:18px;white-space:nowrap}
.fcol a{display:block;font-size:12px;color:#d9dde1;text-decoration:none;line-height:27.5px}
.contact{left:159px;font-size:11.5px;color:#d9dde1;display:flex;gap:8px;line-height:16px}
.social{top:3445px;width:20px;height:20px;border:1px solid #aab;border-radius:50%}
</style>
</head>
<body>

<!-- header -->
<div class="abs topbar"></div>
<div class="abs brand"><div class="brand-dot"></div><div class="brand-name">Marcus Fenwick<br>Consulting</div></div>
<nav>
  <span class="nav-link on" style="left:323px">HOME</span>
  <span class="nav-link" style="left:382px">JOBS</span>
  <span class="nav-link" style="left:434px">EMPLOYERS</span>
  <span class="nav-link" style="left:526px">CANDIDATES</span>
  <span class="nav-link" style="left:620px">PACKAGES</span>
  <span class="nav-link" style="left:702px">PAGES</span>
</nav>
<svg class="abs" style="top:32px;left:777px" width="16" height="18" viewBox="0 0 16 18" fill="none" stroke="#444" stroke-width="1.4"><path d="M3 13V8a5 5 0 0110 0v5l2 2H1z"/><path d="M6 16a2 2 0 004 0"/></svg>
<div class="abs auth" style="left:820px">REGISTER</div>
<div class="abs auth" style="left:899px">SIGN IN</div>
<div class="btn" style="top:18px;left:971px;width:170px;height:44px">
  <svg width="12" height="12" viewBox="0 0 12 12" fill="none" stroke="#fff" stroke-width="1.4"><path d="M6 9V1M3 4l3-3 3 3M1 8v3h10V8"/></svg>POST NEW JOB</div>

<!-- hero -->
<section class="abs hero" role="img" aria-label="Boardroom with long table and chairs beside tall windows, purple tint"></section>
<h1 class="abs head hero-title center">Aim higher. Reach farther.<br>Dream bigger.</h1>
<div class="abs search">
  <div class="f" style="width:229px;font-weight:500">IJob Title, Keywords, Or Phrase</div>
  <div class="f" style="width:165px;justify-content:space-between;padding-right:8px;color:#777">Location
    <svg width="14" height="14" viewBox="0 0 14 14" fill="none" stroke="#bbb"><circle cx="7" cy="7" r="4"/><path d="M7 0v3M7 11v3M0 7h3M11 7h3"/></svg></div>
  <div class="f" style="width:235px;border:none;justify-content:space-between;padding-right:22px;color:#999">Select Sector
    <svg width="9" height="6" viewBox="0 0 9 6" fill="none" stroke="#555" stroke-width="1.4"><path d="M1 1l3.5 3.5L8 1"/></svg></div>
  <div class="go"><svg width="15" height="15" viewBox="0 0 15 15" fill="none" stroke="#fff" stroke-width="2.2"><circle cx="6" cy="6" r="4.5"/><path d="M9.5 9.5L14 14"/></svg></div>
</div>
<div class="abs ghost" style="left:432px;width:208px">
  <svg width="16" height="12" viewBox="0 0 16 12" fill="none" stroke="#fff" stroke-width="1.2"><path d="M4 11H3a3 3 0 010-6 5 5 0 019.5-1A3.5 3.5 0 0113 11h-1M8 11V6M6 8l2-2 2 2"/></svg>Upload Your Resume</div>
<div class="abs ghost" style="left:650px;width:241px">
  <svg width="14" height="12" viewBox="0 0 14 12" fill="none" stroke="#fff" stroke-width="1.2"><rect x="1" y="3" width="12" height="8"/><path d="M5 3V1h4v2"/></svg>Hiring? Post a job for free</div>

<!-- stats -->
<div class="abs stat" style="left:196px"><b>123,012</b><i>Jobs Added</i></div>
<div class="abs vline" style="left:441px"></div>
<div class="abs stat" style="left:490px"><b>187,432</b><i>Active Resumes</i></div>
<div class="abs vline" style="left:747px"></div>
<div class="abs stat" style="left:783px"><b>140,312</b><i>Positions Matched</i></div>
<div class="abs" style="top:610px;left:0;width:1200px;height:1px;background:var(--line)"></div>

<!-- categories -->
<h2 class="abs head title" style="top:668px">Popular <em>Job Categories</em></h2>
<p class="abs lead center" style="top:715px;left:250px;width:700px">Lorem ipsum dolor sit amet, consectetur adipiscing elit, sed do eiusmod tempor incididunt ut labore et dolore magna aliqua. Ut enim ad minim veniam,</p>
<div class="abs cat" style="left:167px"><div class="cat-art" role="img" aria-label="Graduation cap illustration"></div><h4>ED UT PERSPICIATIS</h4><p>(5 VACANCIES)</p></div>
<div class="abs cat" style="left:468px"><div class="cat-art" role="img" aria-label="Monitor with heartbeat line illustration"></div><h4>QUIS NOSTRUM EXEITA</h4><p>(2 VACANCIES)</p></div>
<div class="abs cat" style="left:771px"><div class="cat-art" role="img" aria-label="Weather and plants illustration"></div><h4>QUIS AUTEM VEL EUM</h4><p>(1 VACANCIES)</p></div>
<div class="btn" style="top:932px;left:490px;width:221px;height:43px">
  <svg width="16" height="16" viewBox="0 0 16 16" fill="none" stroke="#fff" stroke-width="1.2"><circle cx="8" cy="8" r="6.5"/><path d="M1.5 8h13M8 1.5c-3 3-3 10 0 13M8 1.5c3 3 3 10 0 13"/></svg>BROWSE ALL SECTORS</div>

<!-- promo -->
<section class="abs promo"></section>
<h2 class="abs head promo-title">Millions of jobs.<br><span style="color:var(--blue)">Find the one that’s right<br>for you.</span></h2>
<p class="abs lead" style="top:1273px;left:158px;width:380px">Lorem ipsum dolor sit amet, consectetur adipis cing elit, sed do eiusmod tempor incididunt ut labore et dolore magna aliqua. Ut enim ad minim veni nostrud exercitation ullamco lab...</p>
<div class="btn" style="top:1380px;left:159px;width:202px;height:44px">
  <svg width="13" height="13" viewBox="0 0 13 13" fill="#fff"><path d="M3 1l2 3-1.3 1.3a7 7 0 003.9 3.9L9 8l3 2-1 2.5C5 12 1 8 .5 2z"/></svg>Call 555.201.4470</div>
<div class="abs" style="top:1384px;left:395px;width:36px;height:36px;border-radius:50%;background:#fff;box-shadow:0 2px 8px rgba(0,0,0,.12);display:flex;align-items:center;justify-content:center">
  <div style="width:22px;height:22px;border-radius:50%;background:var(--blue);display:flex;align-items:center;justify-content:center"><svg width="12" height="10" viewBox="0 0 12 10" fill="#fff"><path d="M1 1h10v6H5L2 9.5V7H1z"/></svg></div></div>
<div class="abs tablet"></div>
<div class="abs" style="top:1294px;left:618px;width:5px;height:5px;border-radius:50%;background:#555"></div>
<div class="abs" style="top:1285px;left:1015px;width:20px;height:20px;border-radius:50%;border:1.5px solid #999"></div>
<div class="abs tablet-screen" role="img" aria-label="Illustration of a vacant office chair beside resumes under a magnifying glass"></div>

<!-- featured jobs -->
<h2 class="abs head title" style="top:1609px">Featured <em>Jobs Listings</em></h2>
<p class="abs lead center" style="top:1656px;left:250px;width:700px">Lorem ipsum dolor sit amet, consectetur adipiscing elit, sed do eiusmod tempor incididunt ut labore et dolore magna aliqua. Ut enim ad minim veniam,</p>

<div class="abs job" style="top:1725px;left:158px">
  <div class="logo"><span style="width:60px;height:60px;border-radius:50%;background:#1aa08a;display:block"></span></div>
  <div class="name">Ed ut perspiciatis unde omnis</div><div class="pub">Published 4 years ago</div>
  <svg class="heart" width="13" height="12" viewBox="0 0 13 12" fill="none" stroke="#4caf50" stroke-width="1.2"><path d="M6.5 11L1.5 6A3 3 0 016.5 2a3 3 0 015 4z"/></svg>
  <div class="meta">United State <small>⊕ Automotive Jobs</small></div>
  <div class="tag" style="background:var(--green)">CONSULTING</div>
</div>
<div class="abs job" style="top:1725px;left:608px">
  <div class="logo"><span style="width:60px;height:60px;border-radius:14px;background:#28b3d6;display:block"></span></div>
  <div class="name">Ed ut perspiciatis unde omnis</div><div class="pub">Published 4 years ago</div>
  <svg class="heart" width="13" height="12" viewBox="0 0 13 12" fill="none" stroke="#4caf50" stroke-width="1.2"><path d="M6.5 11L1.5 6A3 3 0 016.5 2a3 3 0 015 4z"/></svg>
  <div class="meta">United State <small>⊕ Automotive Jobs</small></div>
  <div class="tag" style="background:var(--blue)">FULL TIME</div>
</div>
<div class="abs job" style="top:1857px;left:158px">
  <div class="logo"><span style="width:60px;height:60px;border-radius:50%;background:#f08a3c;display:block"></span></div>
  <div class="name">Ed ut perspiciatis unde omnis</div><div class="pub">Published 4 years ago</div>
  <svg class="heart" width="13" height="12" viewBox="0 0 13 12" fill="none" stroke="#4caf50" stroke-width="1.2"><path d="M6.5 11L1.5 6A3 3 0 016.5 2a3 3 0 015 4z"/></svg>
  <div class="meta">United State <small>⊕ Automotive Jobs</small></div>
  <div class="tag" style="background:var(--orange)">FULL TIME</div>
</div>
<div class="abs job" style="top:1857px;left:608px">
  <div class="logo"><span style="width:60px;height:60px;background:#2b2b2b;display:block"></span></div>
  <div class="name">Ed ut perspiciatis unde omnis</div><div class="pub">Published 4 years ago</div>
  <svg class="heart" width="13" height="12" viewBox="0 0 13 12" fill="none" stroke="#4caf50" stroke-width="1.2"><path d="M6.5 11L1.5 6A3 3 0 016.5 2a3 3 0 015 4z"/></svg>
  <div class="meta">United State <small>⊕ Automotive Jobs</small></div>
  <div class="tag" style="background:var(--green)">CONSULTING</div>
</div>

<!-- research -->
<section class="abs research-bg"></section>
<div class="abs research-photo" role="img" aria-label="Golf course lawn with lamp post, flower beds and trees"></div>
<h2 class="abs head research-title">Marcus Fenwick Consulting<br><span style="color:var(--blue)">Research &amp; Reports</span></h2>
<p class="abs lead" style="top:2225px;left:638px;width:385px">Lorem ipsum dolor sit amet, consectetur adipis cing elit, sed do eiusmod tempor incididunt ut labore et dolore magna aliqua. Ut enim ad minim veni nostrud exercitation ullamco lab...</p>
<p class="abs lead" style="top:2324px;left:638px;width:385px">Lorem ipsum dolor sit amet, consectetur adipis cing elit, sed do eiusmod tempor</p>
<div class="btn" style="top:2395px;left:639px;width:202px;height:44px">
  <svg width="13" height="13" viewBox="0 0 13 13" fill="#fff"><path d="M3 1l2 3-1.3 1.3a7 7 0 003.9 3.9L9 8l3 2-1 2.5C5 12 1 8 .5 2z"/></svg>Call 555.201.4470</div>

<!-- testimonials -->
<h2 class="abs head title" style="top:2603px">What our <em>Clients Say</em></h2>
<p class="abs lead center" style="top:2649px;left:250px;width:700px">Lorem ipsum dolor sit amet, consectetur adipiscing elit, sed do eiusmod tempor incididunt ut labore et dolore magna aliqua. Ut enim ad minim veniam,</p>
<div class="abs quote" style="left:173px">
  <div class="avatar"><span class="badge" style="background:#d9e4cf"></span><span class="q">“</span></div>
  <p>The quality and value the facility gets from Marcus Fenwick is off the charts...highly recommended!</p>
  <h5>Owen Hartley</h5><small>Head Golf Professional</small>
</div>
<div class="abs quote" style="left:481px">
  <div class="avatar"><span class="badge"></span><span class="q">“</span></div>
  <p>Without question, Marcus Fenwick raised the bar with dozens of qualified applicants that fit the end goal criteria.</p>
  <h5>Paul Verano</h5><small>Director of Landscape</small>
</div>
<div class="abs quote" style="left:793px">
  <div class="avatar"><span class="badge"></span><span class="q">“</span></div>
  <p>Thank you so much for a terrific and seamless process. It was a pleasure to work with you.</p>
  <h5>Clara Beaumont</h5><small>General Manager</small>
</div>

<div class="abs center" style="top:3018px;left:0;width:1200px;font-size:14px;font-weight:600;letter-spacing:1.5px;color:#333">AS SEEN IN</div>
<div class="abs seen" style="left:156px"><span></span></div>
<div class="abs seen" style="left:336px"><span style="background:#e4ead6"></span></div>
<div class="abs seen" style="left:517px"><span style="background:#e9dcd6"></span></div>
<div class="abs seen" style="left:698px"><span style="background:#dfe8df"></span></div>
<div class="abs seen" style="left:879px"><span style="background:#d6e6dc"></span></div>

<!-- footer -->
<footer class="abs footer"></footer>
<div class="abs foot-brand"><div class="brand-dot"></div><div class="brand-name">Marcus Fenwick<br>Consulting</div></div>
<div class="abs contact" style="top:3385px">
  <svg width="10" height="13" viewBox="0 0 10 13" fill="#fff"><path d="M5 0a5 5 0 015 5c0 3.5-5 8-5 8S0 8.5 0 5a5 5 0 015-5zm0 3a2 2 0 100 4 2 2 0 000-4z"/></svg>
  <span>48 Fairway Lane, Millbrook,<br>Pennsylvania 17000, United States</span></div>
<div class="abs contact" style="top:3427px;color:var(--blue)">
  <svg width="11" height="11" viewBox="0 0 13 13" fill="#fff"><path d="M3 1l2 3-1.3 1.3a7 7 0 003.9 3.9L9 8l3 2-1 2.5C5 12 1 8 .5 2z"/></svg>555.201.4470</div>
<div class="abs contact" style="top:3455px">
  <svg width="12" height="10" viewBox="0 0 12 10" fill="#fff"><path d="M0 0h12v10H0zm1 1.5V9h10V1.5L6 5.5z"/></svg>hello@marcusfenwick.example</div>

<div class="abs fcol" style="left:431px"><h6>OUR LINKS</h6><a>Home</a><a>Jobs</a><a>Employers</a><a>Candidates</a><a>Packages</a><a>Pages</a></div>
<div class="abs fcol" style="left:614px"><h6>FOR CANDIDATES</h6><a>User Dashboard</a><a>CV Packages</a><a>Candidate Listing</a><a>Candidates Grid</a><a>About us</a></div>
<div class="abs fcol" style="left:844px"><h6>STAY WITH US</h6></div>
<div class="abs" style="top:3326px;left:844px;font-size:12px;color:#cfd3d7">Enter Your Email</div>
<div class="abs" style="top:3360px;left:844px;width:208px;height:1px;background:#55606a"></div>
<div class="btn" style="top:3365px;left:844px;width:137px;height:39px;font-size:13px">SUBSCRIBE</div>
<div class="abs social" style="left:845px"></div>
<div class="abs social" style="left:875px"></div>
<div class="abs social" style="left:905px"></div>
<div class="abs social" style="left:935px"></div>
<div class="abs" style="top:3550px;left:0;width:1200px;height:1px;background:#3a434b"></div>
<div class="abs center" style="top:3572px;left:0;width:1200px;font-size:11px;color:#cfd3d7">© Copyright 2022 Marcus Fenwick Consulting . All rights reserved.</div>

</body>
</html>
```